PowerPoint Re-Design and Template Needs a Designer's Eye!

I have the text, images and logo for a PowerPoint but need your Design and Template skills! Less than 20 pages, needs to be concise, include images, must have creative page layouts, include our floater-logo on every page, use sidebars or call-outs for important information, have color but not too much because this will be printed many times (our current colors are too dark). You can use bullet-points or paragraphs. You can also change the titles, font, color, layout - anything! This is YOUR PowerPoint to create the most impressive Template! We are an investment management firm located in New York City. Our investment returns are the very best in the industry and we want this PowerPoint to convey our "best in class" style.

Notes:
1) Please use the PPP outline attached.
2) I have attached a rough draft PPP. Please use the logos on page 2. Some pages do not have text, the final text will be available shortly.
3) I have attached examples you can reference.
4) Please include our floater-logo on every page.
5) Please feel free to ask questions or clarification.
Updates

Hi Designers, Thank you very much for your wonderful submissions! My partners and I are going through each submission in detail today and tomorrow. We'll be in touch over the next few days with additional questions and comments. Stay tuned! Best, Norman Pasquale

Target Market(s)

High-net worth individuals and institutions. New York City, Wall Street.

Industry/Entity Type

Investment

Requirements
Must have
• - Floater-logo on every page
- Sidebars or call-outs on several pages (you can decide which ones)
- Please include images; however, the PPP Template is the most important.

```html
<!DOCTYPE html>
<html lang="en">
<head>
<meta charset="utf-8">
<title>Investment Presentation Template</title>
<link href="https://fonts.googleapis.com/css2?family=Open+Sans:wght@400;600;700&display=swap" rel="stylesheet">
<style>
  :root{
    --stage:#5f5f61;
    --paper:#ffffff;
    --ink:#1e1e1e;
    --text:#333333;
    --muted:#9a9a9a;
    --rule:#8a8a8a;
    --orange:#e8772e;
    --orange-deep:#d9782b;
    --orange-mid:#f0a060;
    --peach:#f7c4a3;
    --peach-soft:#f9c9a6;
    --tag:#111111;
  }
  *{box-sizing:border-box;margin:0;padding:0}
  html,body{width:1200px;height:848px;overflow:hidden}
  body{background:var(--stage);font-family:"Open Sans",Arial,sans-serif;color:var(--text);position:relative}
  .slide{position:absolute;background:var(--paper);overflow:hidden}
  .slide--summary{left:80px;top:36px;width:510px;height:383px}
  .slide--track{left:630px;top:30px;width:512px;height:383px}
  .slide--philosophy{left:80px;top:431px;width:518px;height:387px}
  .slide--universe{left:636px;top:431px;width:512px;height:384px}

  .page-tag{position:absolute;top:0;width:22px;height:30px;background:var(--tag);color:#fff;font-size:8px;text-align:center;line-height:22px;clip-path:polygon(0 0,100% 0,100% 75%,50% 100%,0 75%)}
  .slide-title{position:absolute;font-size:17px;font-weight:400;color:var(--ink);letter-spacing:.2px;white-space:nowrap}
  .slide-title .accent{color:var(--orange);font-weight:700}
  .footer-credit{position:absolute;left:0;right:0;text-align:center;font-size:7px;color:var(--muted)}
  .brand{position:absolute;display:flex;align-items:center;gap:3px;font-size:8px;font-weight:600;color:var(--orange)}
  .brand-dot{width:16px;height:16px;border-radius:50%;background:var(--orange)}

  /* Executive summary */
  .summary-divider{position:absolute;left:125px;top:97px;width:1px;height:215px;background:var(--rule)}
  .summary-label{position:absolute;left:28px;width:89px;text-align:center;font-size:10.5px;color:var(--ink);line-height:15px;border-bottom:1px solid var(--rule);padding-bottom:2px}
  .summary-text{position:absolute;left:144px;width:348px;font-size:10px;color:var(--ink);line-height:14px;border-bottom:1px solid var(--rule);padding:0 14px 3px 16px;text-indent:-6px}

  /* Philosophy */
  .hero{position:absolute;left:0;top:0;width:518px;height:155px;background:linear-gradient(180deg,#b8642a 0%,#d98a45 45%,#e9a35e 70%,#c97a3a 100%)}
  .hero-stones{position:absolute;left:345px;top:15px;width:110px;height:140px;background:radial-gradient(ellipse at 50% 60%,#d9a070 0%,rgba(217,160,112,.6) 50%,rgba(217,160,112,0) 75%)}
  .hero-title{position:absolute;left:80px;top:60px;font-size:19px;font-weight:400;color:#fff;letter-spacing:.3px}
  .body-copy{position:absolute;font-size:7.3px;line-height:11px;color:var(--ink)}
  .body-copy p{margin-bottom:13px}
  .slide--philosophy .body-copy{left:36px;top:183px;width:436px;font-size:7.6px}

  /* Universe */
  .universe-art{position:absolute;left:0;top:0}
  .city-shot{position:absolute;left:34px;width:150px}
  .city-shot--night{top:115px;height:54px;background:linear-gradient(180deg,#2b2a3a,#6b5a48 60%,#3a2f2a)}
  .city-shot--day{top:173px;height:46px;background:linear-gradient(180deg,#b9c8d6,#8aa0b4 55%,#5c6f80)}
  .city-shot--shore{top:222px;height:41px;background:linear-gradient(180deg,#c9d2d8,#a7a98e 55%,#6f7656)}
  .slide--universe .body-copy{left:221px;top:97px;width:252px;font-size:8.2px;line-height:12.3px;text-align:justify}
  .slide--universe .body-copy p{margin-bottom:10px}
  .bullet-list{list-style:none;margin-top:6px}
  .bullet-list li{margin-bottom:12px;padding-left:0;text-align:left}
</style>
</head>
<body>

<section class="slide slide--summary">
  <div class="page-tag" style="left:442px">03</div>
  <h1 class="slide-title" style="left:26px;top:27px">EXECUTIVE <span class="accent">SUMMARY</span></h1>
  <div class="summary-divider"></div>

  <div class="summary-label" style="top:100px">Strategy</div>
  <div class="summary-text" style="top:102px">• Long-only value investing &nbsp;with multiple hedging strategies.</div>

  <div class="summary-label" style="top:160px">Objective</div>
  <div class="summary-text" style="top:148px">• To compound our principle using superior risk management while providing liquidity and full transparency to our clients.</div>

  <div class="summary-label" style="top:199px">Investment Approach</div>
  <div class="summary-text" style="top:202px">• Research driven fundamental analysis at the quantitative and qualitative levels.</div>

  <div class="summary-label" style="top:259px">Alignment of Interest</div>
  <div class="summary-text" style="top:262px">• Company owned with over 90% of Founder’s net worth invested in the same strategy.</div>

  <div class="footer-credit" style="top:368px">Norman Pasquale 2015</div>
  <div class="brand" style="left:448px;top:352px"><span class="brand-dot"></span>Quillmere</div>
</section>

<section class="slide slide--track">
  <div class="page-tag" style="left:445px">04</div>
  <h1 class="slide-title" style="left:28px;top:27px">PERFORMANCE <span class="accent">TRACK RECORD</span></h1>

  <svg class="chart" style="position:absolute;left:90px;top:82px" width="340" height="230" viewBox="0 0 340 230" font-family="Open Sans, Arial, sans-serif">
    <text x="152" y="16" text-anchor="middle" font-size="12" font-weight="700" fill="#1e1e1e">Dummy Chart</text>
    <text transform="translate(16,93) rotate(-90)" text-anchor="middle" font-size="7" font-weight="700" fill="#1e1e1e">Axis Title</text>
    <g stroke="#bdbdbd" stroke-width="0.8">
      <line x1="48" y1="33" x2="330" y2="33"/><line x1="48" y1="46.3" x2="330" y2="46.3"/>
      <line x1="48" y1="59.7" x2="330" y2="59.7"/><line x1="48" y1="73" x2="330" y2="73"/>
      <line x1="48" y1="86.3" x2="330" y2="86.3"/><line x1="48" y1="99.7" x2="330" y2="99.7"/>
      <line x1="48" y1="113" x2="330" y2="113"/><line x1="48" y1="126.3" x2="330" y2="126.3"/>
      <line x1="48" y1="139.7" x2="330" y2="139.7"/><line x1="48" y1="153" x2="330" y2="153"/>
    </g>
    <g font-size="10" fill="#1e1e1e" text-anchor="end">
      <text x="38" y="37">10</text><text x="38" y="50">8</text><text x="38" y="63">6</text>
      <text x="38" y="77">4</text><text x="38" y="90">2</text><text x="38" y="103">0</text>
      <text x="38" y="117">-2</text><text x="38" y="130">-4</text><text x="38" y="143">-6</text><text x="38" y="157">-8</text>
    </g>
    <g fill="var(--orange-deep)">
      <rect x="54" y="99.7" width="9" height="28.7"/><rect x="94.3" y="83" width="9" height="16.7"/>
      <rect x="134.6" y="76.4" width="9" height="23.3"/><rect x="174.9" y="69.7" width="9" height="30"/>
      <rect x="215.2" y="72.4" width="9" height="27.3"/><rect x="255.5" y="71.3" width="9" height="28.4"/>
      <rect x="295.8" y="70.2" width="9" height="29.5"/>
    </g>
    <g fill="var(--orange-mid)">
      <rect x="63" y="83.7" width="9" height="16"/><rect x="103.3" y="70.4" width="9" height="29.3"/>
      <rect x="143.6" y="99.7" width="9" height="12"/><rect x="183.9" y="81" width="9" height="18.7"/>
      <rect x="224.2" y="83" width="9" height="16.7"/><rect x="264.5" y="84" width="9" height="15.7"/>
      <rect x="304.8" y="84.9" width="9" height="14.8"/>
    </g>
    <g fill="var(--peach)">
      <rect x="72" y="86.4" width="9" height="13.3"/><rect x="112.3" y="86.4" width="9" height="13.3"/>
      <rect x="152.6" y="79.7" width="9" height="20"/><rect x="192.9" y="66.4" width="9" height="33.3"/>
      <rect x="233.2" y="99.7" width="9" height="36.7"/><rect x="273.5" y="56.4" width="9" height="43.3"/>
      <rect x="313.8" y="49.7" width="9" height="50"/>
    </g>
    <g stroke="#bdbdbd" stroke-width="0.8" fill="none">
      <rect x="48" y="155" width="282" height="18"/>
      <rect x="14" y="173" width="316" height="48"/>
      <line x1="14" y1="189" x2="330" y2="189"/><line x1="14" y1="205" x2="330" y2="205"/>
      <line x1="48" y1="155" x2="48" y2="221"/><line x1="88.3" y1="155" x2="88.3" y2="221"/>
      <line x1="128.6" y1="155" x2="128.6" y2="221"/><line x1="168.9" y1="155" x2="168.9" y2="221"/>
      <line x1="209.2" y1="155" x2="209.2" y2="221"/><line x1="249.5" y1="155" x2="249.5" y2="221"/>
      <line x1="289.8" y1="155" x2="289.8" y2="221"/>
    </g>
    <g font-size="7.5" font-weight="700" fill="#1e1e1e" text-anchor="middle">
      <text x="68" y="167">Stage 1</text><text x="108.5" y="167">Stage 2</text><text x="148.8" y="167">Stage 3</text>
      <text x="189" y="167">Stage 4</text><text x="229.4" y="167">Stage 5</text><text x="269.7" y="167">Stage 6</text><text x="310" y="167">Stage 7</text>
    </g>
    <rect x="17" y="178" width="6" height="6" fill="var(--orange-deep)"/>
    <rect x="17" y="194" width="6" height="6" fill="var(--orange-mid)"/>
    <rect x="17" y="210" width="6" height="6" fill="var(--peach)"/>
    <g font-size="8" fill="#1e1e1e">
      <text x="26" y="184">1988</text><text x="26" y="200">1999</text><text x="26" y="216">2009</text>
    </g>
    <g font-size="8.5" fill="#1e1e1e" text-anchor="middle">
      <text x="68" y="184">-4.3</text><text x="108.5" y="184">2.5</text><text x="148.8" y="184">3.5</text><text x="189" y="184">4.5</text><text x="229.4" y="184">4.1</text><text x="269.7" y="184">4.26</text><text x="310" y="184">4.42</text>
      <text x="68" y="200">2.4</text><text x="108.5" y="200">4.4</text><text x="148.8" y="200">-1.8</text><text x="189" y="200">2.8</text><text x="229.4" y="200">2.5</text><text x="269.7" y="200">2.36</text><text x="310" y="200">2.22</text>
      <text x="68" y="216">2</text><text x="108.5" y="216">2</text><text x="148.8" y="216">3</text><text x="189" y="216">5</text><text x="229.4" y="216">-5.5</text><text x="269.7" y="216">6.5</text><text x="310" y="216">7.5</text>
    </g>
  </svg>

  <div class="footer-credit" style="top:372px">Norman Pasquale 2015</div>
  <div class="brand" style="left:450px;top:352px"><span class="brand-dot"></span>Quillmere</div>
</section>

<section class="slide slide--philosophy">
  <div class="hero" role="img" aria-label="Photograph of balanced stacked stones against an orange sunset sky">
    <div class="hero-stones"></div>
  </div>
  <h1 class="hero-title">OUR PHYLOSOPHY</h1>
  <div class="body-copy">
    <p>We are long-term investors who buy deeply valued securities in companies we want to own. We are contrarian in nature and seek opportunities with strong cash flow, inexpensive assets and multiple competitive advantages.</p>
    <p>We are thematic at the macro-level and use a bottom-up, research-intensive evaluation process at the sector and security level. This process includes analyzing securities at the quantitative and qualitative levels.</p>
    <p>Risk is a significant focus that often keeps us inactive and sitting with cash. The securities we purchase are the ones remaining after risk-analysis.</p>
    <p>Our size per position varies for many reasons and is used as a form of risk management.</p>
  </div>
  <div class="footer-credit" style="top:375px">Norman Pasquale 2015</div>
  <div class="brand" style="left:455px;top:353px"><span class="brand-dot"></span>Quillmere</div>
</section>

<section class="slide slide--universe">
  <svg class="universe-art" width="200" height="384" viewBox="0 0 200 384" aria-hidden="true">
    <polygon points="4,0 84,0 106,118 30,118" fill="var(--peach-soft)"/>
    <polygon points="30,262 150,262 126,384 0,384 0,300" fill="var(--orange)"/>
  </svg>
  <div class="city-shot city-shot--night" role="img" aria-label="Photograph of a city skyline at night"></div>
  <div class="city-shot city-shot--day" role="img" aria-label="Photograph of a city skyline by day"></div>
  <div class="city-shot city-shot--shore" role="img" aria-label="Photograph of a waterfront city"></div>

  <h1 class="slide-title" style="left:209px;top:27px">STRATEGY<span class="accent">: INVESTMENT UNIVERSE</span></h1>
  <div class="body-copy">
    <p>To purchase domestic and foreign securities that offer superior risk-adjusted returns. We are thematic at the macro-level and use a bottom-up, research-intensive evaluation process at the sector and security level.</p>
    <p>Of significant importance to us is evaluating opportunities at both the quantitative and qualitative levels. Once a security has been selected for investment, a risk-budget is assigned to it based on possible outcomes and the potential risk/reward ratio.</p>
    <ul class="bullet-list">
      <li>• Long-biased small, mid and large cap domestic and foreign securities.</li>
      <li>• Hold 20-35 positions from several months to many years.</li>
      <li>• All dividends are used to purchase additional securities.</li>
    </ul>
  </div>
  <div class="footer-credit" style="top:371px">Norman Pasquale 2015</div>
  <div class="brand" style="left:452px;top:352px"><span class="brand-dot"></span>Quillmere</div>
</section>

</body>
</html>
```